Lantern Over Maple Book Cover Design

We need:

Ebook and 6x 9 Inch trade paperback book cover (front, back, spine)

Book Title:Lantern Over Maple
Subtitle: Seven Steps Toward Ordering Every Household Matter Before Trouble Arrives Unannounced

For a book written to help any of us gather the information needed to ensure we are set to take care of our loved ones in case of an emergency. Loved ones, a sense of urgency that leads to feeling calm and prepared is needed!

Target Market(s)

Any adult with children, a partner, parents or assets!

Industry/Entity Type

Financial Planning, Health care, Family

Font styles to use
Serif
Sans Serif

Colors
0054AA
0677BA
7BADD7
CADEEF
E8F1F8
FFF300
FFF600
FEFA6F
FFFEC7
FFFEE8
EE7325
F08F49
F5BC92
FAE3D3
FDF4ED
EB3D1F
EC4F4E
F09395
F8D3D4
FCEDEE

```html
<!DOCTYPE html>
<html lang="en">
<head>
<meta charset="utf-8">
<title>Lantern Over Maple – Cover Spread</title>
<link href="https://fonts.googleapis.com/css2?family=Anton&family=Kaushan+Script&family=Oswald:wght@400&family=Cormorant+Garamond:ital,wght@1,500&display=swap" rel="stylesheet">
<style>
  :root {
    --stage: #a6a29f;
    --paper: #ffffff;
    --paper-tint: #e8f1f8;
    --band-back: #0677ba;
    --band-top: #cadeef;
    --ink: #0054aa;
    --spine-ink: #0677ba;
    --photo-light: #e8f1f8;
    --photo-mid: #7badd7;
    --photo-dark: #0054aa;
    --title: #fffee8;
    --accent-warm: #f08f49;
    --accent-soft: #fae3d3;
    --accent-red: #eb3d1f;
    --portrait: #0054aa;
  }
  * { margin: 0; padding: 0; box-sizing: border-box; }
  html, body { width: 1200px; height: 1200px; overflow: hidden; }
  body { background: var(--stage); position: relative; }

  .back-cover {
    position: absolute; left: 140px; top: 302px; width: 389px; height: 588px;
    background: linear-gradient(90deg, var(--paper) 0%, var(--paper-tint) 100%);
  }
  .back-cover .side-band {
    position: absolute; right: 22px; top: 0; width: 104px; height: 100%;
    background: linear-gradient(180deg, var(--band-back) 0%, var(--photo-mid) 100%);
  }
  .back-cover .author-portrait {
    position: absolute; right: 22px; bottom: 0; width: 104px; height: 182px;
    background: linear-gradient(180deg, var(--photo-mid) 0%, var(--accent-soft) 35%, var(--accent-warm) 62%, var(--portrait) 82%);
  }

  .spine {
    position: absolute; left: 576px; top: 302px; width: 46px; height: 588px;
    background: var(--paper);
    border-left: 4px solid var(--accent-warm);
    display: flex; align-items: center; justify-content: center;
  }
  .spine-text {
    transform: rotate(-90deg); white-space: nowrap;
    font-family: "Cormorant Garamond", serif; font-style: italic; font-weight: 500;
    font-size: 19px; color: var(--spine-ink); letter-spacing: 0.5px;
  }
  .spine-text .divider { margin: 0 14px; color: var(--accent-red); }

  .front-cover {
    position: absolute; left: 664px; top: 302px; width: 421px; height: 588px;
    background: var(--paper);
  }
  .front-art {
    position: absolute; left: 53px; top: 0; width: 368px; height: 100%;
    overflow: hidden;
  }
  .cover-photo {
    position: absolute; inset: 0;
    background:
      radial-gradient(ellipse at 40% 75%, rgba(240,143,73,0.55) 0%, rgba(240,143,73,0) 45%),
      radial-gradient(ellipse at 55% 40%, var(--photo-light) 0%, var(--photo-mid) 55%, var(--photo-dark) 100%);
  }
  .author-band {
    position: absolute; left: 0; top: 0; width: 100%; height: 38px;
    background: var(--band-top);
    display: flex; align-items: center; justify-content: center;
    font-family: "Oswald", sans-serif; font-size: 17px; color: var(--ink);
  }
  .book-title {
    position: absolute; left: 0; top: 50px; width: 100%;
    text-align: center; font-family: "Anton", sans-serif; font-weight: 400;
    font-size: 72px; line-height: 70px; color: var(--title);
    text-transform: uppercase; letter-spacing: 1px;
    text-shadow: 0 2px 6px rgba(0,84,170,0.35);
  }
  .book-subtitle {
    position: absolute; left: 24px; right: 24px; bottom: 22px;
    text-align: center; font-family: "Kaushan Script", cursive;
    font-size: 14px; line-height: 22px; color: var(--title);
    text-shadow: 0 1px 3px rgba(0,0,0,0.55);
  }
</style>
</head>
<body>
  <section class="back-cover">
    <div class="side-band"></div>
    <div class="author-portrait" role="img" aria-label="Author portrait photograph"></div>
  </section>

  <section class="spine">
    <div class="spine-text">Lantern Over Maple<span class="divider">|</span>Delia Marsh</div>
  </section>

  <section class="front-cover">
    <div class="front-art">
      <div class="cover-photo" role="img" aria-label="Photograph of a grey-haired woman in a tan blazer writing in a notebook against a soft backdrop"></div>
      <div class="author-band">Delia Marsh</div>
      <h1 class="book-title">Lantern<br>Over<br>Maple</h1>
      <p class="book-subtitle">Seven Steps Toward Ordering Every Household Matter Before Trouble Arrives Unannounced</p>
    </div>
  </section>
</body>
</html>
```